kvt business card

need clean and modern business card design, possibly two. Logo on front and writing on back-Full source files for logo attached-THE CHOSEN LOGO IS SQUARE KVT with KVT HOLDINGS in ALL BLUE. Please do not use any other logos from files, this is source file that includes correct logo

```html
<!DOCTYPE html>
<html lang="en">
<head>
<meta charset="utf-8">
<title>KVT Holdings Business Cards</title>
<link rel="stylesheet" href="https://fonts.googleapis.com/css2?family=Michroma&family=Arimo:wght@400;700&display=swap">
<style>
  :root {
    --blue: #2f86c4;
    --blue-deep: #2a6fae;
    --blue-light: #4aa6d6;
    --green: #a9cc3a;
    --ink: #3d6f9c;
    --grey-text: #6c8aa5;
    --card: #ffffff;
    --page: #ececea;
  }
  * { margin: 0; padding: 0; box-sizing: border-box; }
  html, body { width: 1200px; height: 780px; overflow: hidden; background: var(--page); }
  .canvas { position: relative; width: 1200px; height: 780px; }
  .card {
    position: absolute; width: 560px; height: 320px;
    background: var(--card); border-radius: 18px; overflow: hidden;
    box-shadow: 0 6px 18px rgba(0,0,0,0.15);
  }
  .card-front { left: 50px; top: 60px; }
  .card-back { left: 590px; top: 400px; }
  .card svg.bands { position: absolute; inset: 0; }
  .brand { position: absolute; font-family: "Michroma", sans-serif; white-space: nowrap; }
  .brand-mark {
    position: absolute; left: 40px; top: 96px; width: 64px; height: 64px;
    border: 7px solid var(--blue);
  }
  .front-name { left: 40px; top: 178px; font-size: 28px; color: var(--blue); letter-spacing: 1px; }
  .front-tagline { left: 42px; top: 220px; font-size: 9.5px; color: var(--green); letter-spacing: 1px; }
  .contact {
    position: absolute; right: 118px; top: 24px; text-align: right;
    font-family: "Arimo", sans-serif; font-style: normal; color: var(--grey-text); font-size: 12px; line-height: 1.55;
  }
  .contact .person { font-family: "Michroma", sans-serif; color: var(--ink); font-size: 14px; font-weight: 700; }
  .contact .role { color: var(--green); font-size: 12px; margin-bottom: 8px; }
  .website {
    position: absolute; right: 20px; bottom: 20px;
    font-family: "Arimo", sans-serif; color: #fff; font-size: 12px; letter-spacing: 0.5px;
  }
  .back-name { left: 0; right: 0; top: 132px; text-align: center; font-size: 38px; color: var(--blue); letter-spacing: 2px; }
  .back-tagline { left: 0; right: 0; top: 186px; text-align: center; font-size: 12px; color: var(--green); letter-spacing: 1.5px; }
</style>
</head>
<body>
<main class="canvas">
  <section class="card card-front" aria-label="Business card front">
    <svg class="bands" width="560" height="320" viewBox="0 0 560 320" aria-hidden="true">
      <defs>
        <linearGradient id="front-blue" x1="0" y1="1" x2="1" y2="0">
          <stop offset="0" stop-color="var(--blue-deep)"/>
          <stop offset="0.6" stop-color="var(--blue-light)"/>
          <stop offset="1" stop-color="var(--blue)"/>
        </linearGradient>
      </defs>
      <path d="M372,320 C450,232 510,124 560,14 L560,30 C516,136 462,240 392,320 Z" fill="var(--green)"/>
      <path d="M404,320 C474,240 522,134 560,40 L560,320 Z" fill="url(#front-blue)"/>
    </svg>
    <div class="brand-mark"></div>
    <div class="brand front-name">KVT HOLDINGS</div>
    <div class="brand front-tagline">KESTREL VALE TRADING GROUP</div>
    <address class="contact">
      <div class="person">DARA QUILL</div>
      <div class="role">Founder</div>
      <div>PO BOX 456 your address</div>
      <div>4th lane Ashford</div>
      <div>(555) 010-2468</div>
      <div>hello@kvtmail.com</div>
    </address>
    <div class="website">www.KVTSITE.com</div>
  </section>

  <section class="card card-back" aria-label="Business card back">
    <svg class="bands" width="560" height="320" viewBox="0 0 560 320" aria-hidden="true">
      <defs>
        <linearGradient id="back-blue" x1="0" y1="0" x2="1" y2="1">
          <stop offset="0" stop-color="var(--blue-light)"/>
          <stop offset="1" stop-color="var(--blue-deep)"/>
        </linearGradient>
      </defs>
      <path d="M0,0 H560 V132 C420,66 220,34 0,22 Z" fill="url(#back-blue)"/>
      <path d="M0,30 C220,42 420,76 560,144 L560,156 C420,90 220,50 0,36 Z" fill="var(--green)"/>
      <path d="M0,320 V196 C140,258 340,286 560,292 V320 Z" fill="url(#back-blue)"/>
      <path d="M0,178 C140,240 340,272 560,280 L560,286 C340,280 140,252 0,190 Z" fill="var(--green)"/>
    </svg>
    <div class="brand back-name">KVT HOLDINGS</div>
    <div class="brand back-tagline">KESTREL VALE TRADING GROUP</div>
  </section>
</main>
</body>
</html>
```